Website design for new health & wellness company

We need our website to be designed in a user friendly way. Needs to be aesthetically pleasing to viewer and easy to navigate and upload content for our small team . The logo should be completely redesigned , please do not reference the current one thats on our site for a starting place. (included below though) We want to move away from that.

the website is : www.brightpathmoments.net

We are a small group of writers/coaches who believe that to change the world you have to be the change and we provide tips/suggestions for every day life that if followed can make a huge difference in your life and overall being.

Target Market(s)

Men and women ages 22 to 50

Industry/Entity Type

Health And Wellness

Logo Text

Cultivate the life of your dreams

Coding

Coded - Design and coding required

Number of Pages Required

3 page

Font styles to use
Sans Serif

Colors

Designer to choose colors to be used in the design.

Requirements
Must have
• Easy to navigate. Mobile friendly. Gender neutral, should appeal to both.

```html
<!DOCTYPE html>
<html lang="en">
<head>
<meta charset="utf-8">
<title>Bright Path Moments – Holistic Approach</title>
<link href="https://fonts.googleapis.com/css2?family=Open+Sans:wght@400;600;700;800&display=swap" rel="stylesheet">
<style>
:root{
  --header-bg:#e6e6e6;
  --page-bg:#e6e9ec;
  --ink:#222222;
  --text:#444444;
  --nav:#333333;
  --accent-teal:#2fb5a3;
  --green-light:#93c324;
  --green-dark:#3a8228;
  --pill-dark:#222222;
  --white:#ffffff;
}
*{box-sizing:border-box;margin:0;padding:0}
html,body{width:1059px;height:1200px;overflow:hidden}
body{font-family:"Open Sans",Arial,sans-serif;background:var(--page-bg);color:var(--text);position:relative}
.site-header{position:absolute;left:0;top:0;width:1059px;height:98px;background:var(--header-bg)}
.brand{position:absolute;left:104px;top:34px;display:flex;align-items:center;gap:7px}
.brand-dot{width:14px;height:14px;border-radius:50%;background:var(--green-dark)}
.brand-name{font-size:16px;font-weight:700;color:var(--green-dark);letter-spacing:.2px}
.search-box{position:absolute;left:817px;top:24px;width:128px;height:16px;border-radius:8px;background:#f3f3f3}
.search-box svg{position:absolute;right:8px;top:2px}
.main-nav{position:absolute;top:58px;left:348px;display:flex;gap:0}
.main-nav a{font-size:12px;letter-spacing:.6px;color:var(--nav);text-decoration:none;position:absolute;white-space:nowrap}
.main-nav a.active{color:var(--accent-teal)}
.hero{position:absolute;left:0;top:98px;width:1059px;height:489px;
  background:
   radial-gradient(circle at 74% 40%,rgba(255,236,140,.95) 0,rgba(247,214,95,.7) 18%,rgba(255,255,255,0) 42%),
   radial-gradient(circle at 9% 63%,rgba(240,230,120,.75) 0,rgba(240,230,120,0) 9%),
   linear-gradient(100deg,#22c9a8 0%,#5fd3bb 25%,#b9e4cf 48%,#f2e7b8 70%,#f6e4b0 100%)}
.hero-photo-area{position:absolute;left:560px;top:45px;width:340px;height:440px}
.hero-copy{position:absolute;left:171px;top:72px;width:380px}
.hero-title{font-size:46px;line-height:42px;font-weight:800;color:var(--ink);letter-spacing:1px}
.hero-lead{margin-top:24px;font-size:17px;font-weight:700;color:var(--ink)}
.hero-text{margin-top:18px;font-size:12.5px;line-height:18.5px;color:var(--ink)}
.btn-light{position:absolute;left:172px;top:306px;width:151px;height:29px;border-radius:15px;background:var(--white);
  box-shadow:2px 3px 4px rgba(0,0,0,.3);font-size:14px;font-weight:600;color:var(--ink);display:flex;align-items:center;justify-content:center;letter-spacing:.4px}
.feature-row{position:absolute;left:109px;top:518px;width:839px;height:185px;display:flex;gap:2.5px}
.feature{flex:1;height:185px;text-align:center;color:var(--white);position:relative}
.feature.light{background:var(--green-light)}
.feature.dark{background:var(--green-dark)}
.feature svg{position:absolute;left:50%;top:20px;transform:translateX(-50%)}
.feature-title{position:absolute;top:93px;width:100%;font-size:13px}
.feature-sub{position:absolute;top:114px;width:100%;font-size:11px}
.pill-more{position:absolute;left:50%;top:140px;transform:translateX(-50%);width:73px;height:24px;border-radius:12px;background:var(--pill-dark);
  color:var(--white);font-size:15px;display:flex;align-items:center;justify-content:center;box-shadow:2px 3px 4px rgba(0,0,0,.35)}
.intro{position:absolute;left:110px;top:768px;width:520px}
.intro h1{font-size:28px;font-weight:400;color:var(--text)}
.intro .intro-sub{margin-top:6px;font-size:15px;color:var(--text)}
.intro p.body{margin-top:20px;font-size:10.7px;line-height:16.8px;width:512px}
.intro h2{margin-top:46px;font-size:15px;font-weight:600;color:var(--text)}
.intro h2 + p.body{margin-top:8px}
.btn-green{position:absolute;left:110px;top:1097px;width:181px;height:36px;border-radius:18px;background:var(--green-dark);color:var(--white);
  font-size:12.5px;font-weight:700;display:flex;align-items:center;justify-content:center;box-shadow:2px 4px 5px rgba(0,0,0,.3)}
.faq-photo{position:absolute;left:659px;top:778px;width:289px;height:288px;
  background:radial-gradient(circle at 50% 45%,#e0b9a0 0,#c99a80 35%,#d9d6d2 70%,#c8c8c8 100%)}
.faq-banner{position:absolute;left:659px;top:1066px;width:290px;height:68px;background:var(--green-dark);color:var(--white);
  text-align:center;font-size:12px;font-weight:600;line-height:18.5px;padding-top:15px}
</style>
</head>
<body>
<header class="site-header">
  <div class="brand"><span class="brand-dot"></span><span class="brand-name">Bright Path Moments</span></div>
  <div class="search-box">
    <svg width="12" height="12" viewBox="0 0 12 12"><circle cx="5" cy="5" r="3.6" fill="none" stroke="#c8c8c8" stroke-width="1.4"/><line x1="7.7" y1="7.7" x2="11" y2="11" stroke="#c8c8c8" stroke-width="1.6"/></svg>
  </div>
  <nav class="main-nav">
    <a class="active" style="left:0">HOME</a>
    <a style="left:66px">ABOUT US</a>
    <a style="left:157px">WORK WITH US</a>
    <a style="left:276px">SUCCESS STORIES</a>
    <a style="left:412px">BLOG</a>
    <a style="left:475px">CONNECT</a>
    <a style="left:562px">MORE</a>
  </nav>
</header>

<section class="hero">
  <div class="hero-photo-area" role="img" aria-label="Silhouette of a person meditating cross-legged on calm sea water at sunrise"></div>
  <div class="hero-copy">
    <div class="hero-title">HOLISTIC<br>APPROACH</div>
    <div class="hero-lead">Get inspired, motivated and active!</div>
    <p class="hero-text">We believe there are more than five senses and we wish people to use the information from all there senses and assist them in developing <b>'uncommon sense'</b></p>
  </div>
  <div class="btn-light">WORK WITH US</div>
</section>

<section class="feature-row">
  <div class="feature light">
    <svg width="52" height="62" viewBox="0 0 52 62" fill="none" stroke="#fff" stroke-width="2.2">
      <rect x="19" y="2" width="14" height="5" rx="1"/><line x1="26" y1="7" x2="26" y2="12"/>
      <circle cx="26" cy="36" r="23"/><line x1="44" y1="14" x2="48" y2="10"/>
      <path d="M26 47 L15 36 a6 6 0 0 1 11-7 a6 6 0 0 1 11 7 Z"/>
    </svg>
    <div class="feature-title">Health Coach Services</div>
    <div class="feature-sub">Work with us</div>
    <div class="pill-more">More</div>
  </div>
  <div class="feature dark">
    <svg width="56" height="60" viewBox="0 0 56 60" fill="none" stroke="#fff" stroke-width="2.2">
      <path d="M28 56 C18 46 18 30 28 18 C38 30 38 46 28 56 Z"/>
      <path d="M28 56 C16 54 6 44 5 30 C16 32 24 40 28 56 Z"/>
      <path d="M28 56 C40 54 50 44 51 30 C40 32 32 40 28 56 Z"/>
      <circle cx="28" cy="8" r="5"/>
    </svg>
    <div class="feature-title">Holistic Approach</div>
    <div class="feature-sub">Meet my associates</div>
    <div class="pill-more">More</div>
  </div>
  <div class="feature light">
    <svg width="60" height="60" viewBox="0 0 60 60" fill="none" stroke="#fff" stroke-width="2.2">
      <circle cx="46" cy="14" r="6"/>
      <g stroke-width="1.8"><line x1="46" y1="2" x2="46" y2="5"/><line x1="58" y1="14" x2="55" y2="14"/><line x1="37" y1="14" x2="34" y2="14"/><line x1="54" y1="6" x2="52" y2="8"/><line x1="54" y1="22" x2="52" y2="20"/><line x1="38" y1="6" x2="40" y2="8"/></g>
      <path d="M2 58 L26 16 L50 58 Z"/><path d="M18 58 L30 44 L40 58"/><path d="M34 30 L40 26 L44 34"/>
    </svg>
    <div class="feature-title">Success Stories</div>
    <div class="feature-sub">Get inspired &amp; motivated</div>
    <div class="pill-more">More</div>
  </div>
  <div class="feature dark">
    <svg width="60" height="56" viewBox="0 0 60 56" fill="none" stroke="#fff" stroke-width="2.2">
      <rect x="2" y="6" width="56" height="48"/><line x1="2" y1="16" x2="58" y2="16"/>
      <g stroke-width="2"><line x1="12" y1="2" x2="12" y2="10"/><line x1="24" y1="2" x2="24" y2="10"/><line x1="36" y1="2" x2="36" y2="10"/><line x1="48" y1="2" x2="48" y2="10"/></g>
      <g fill="#fff" stroke="none"><circle cx="14" cy="26" r="1.6"/><circle cx="24" cy="26" r="1.6"/><circle cx="34" cy="26" r="1.6"/><circle cx="44" cy="26" r="1.6"/><circle cx="14" cy="36" r="1.6"/><circle cx="24" cy="36" r="1.6"/><circle cx="44" cy="36" r="1.6"/><circle cx="14" cy="46" r="1.6"/><circle cx="24" cy="46" r="1.6"/><circle cx="34" cy="46" r="1.6"/></g>
      <rect x="30" y="32" width="8" height="8"/>
    </svg>
    <div class="feature-title">Request an appointment</div>
    <div class="feature-sub">Call me or fill in a form</div>
    <div class="pill-more">More</div>
  </div>
</section>

<section class="intro">
  <h1>Heal your relationship with your body</h1>
  <p class="intro-sub">Holistic loream ipsum support customized to your personal needs.</p>
  <p class="body">Personalized patient care is what sets Verdana Care Center apart. When you visit one of our four San Francisco campus locations you can expect to receive world class care. Expert physician specialists and caring clinical staff provide you with an exceptional health care experience. Personalized patient care is what sets Verdana Care Center apart.</p>
  <h2>Loream Ipsum loream ipsum</h2>
  <p class="body">Loream Ipsum is the personalized patient care is loream Ipsum what sets Verdana Care Center loream Ipsum apart. When you visit loream Ipsum one of our four San Francisco campus loream Ipsum you can expect to receive world class loream Ipsum. Expert physician loream Ipsum specialists and loream Ipsum staff provide you with an exceptional health care experience.</p>
</section>
<div class="btn-green">WORK WITH US</div>

<div class="faq-photo" role="img" aria-label="Smiling woman holding two orange halves in front of her eyes"></div>
<div class="faq-banner">WHAT IS A HEALTH COACH?<br>And other FAQs</div>
</body>
</html>
```